Tello Haulage Junk Removal Postcard

I am looking to have a postcard made for my junk removal company. Details:
size: 6"x9"
I would like to keep it clean and simple. Our company colors are pink, blue and white. You can find the colors and info on the company and what we do on our website which is www.tellohaulage.example .
I've attached a sample of a postcard that was made on ArtHive for another junk removal company. I like the way the attached one looks.

```html
<!DOCTYPE html>
<html lang="en">
<head>
<meta charset="utf-8">
<title>Tello Haulage Postcard</title>
<link rel="stylesheet" href="https://fonts.googleapis.com/css2?family=Roboto+Condensed:wght@700&family=Lato:wght@400;700&display=swap">
<style>
  :root {
    --pink: #e8098b;
    --pink-light: #f25aae;
    --blue: #0c5fb1;
    --blue-deep: #0a4f98;
    --ink: #1d1d1f;
    --white: #ffffff;
    --band-grey: #e4e4e6;
    --stamp: #c9c9cc;
    --rule: #c8c8cc;
    --backdrop: #6c6c6c;
  }
  html, body {
    margin: 0; padding: 0;
    width: 1200px; height: 1200px;
    overflow: hidden;
    background: var(--backdrop);
  }
  .postcard {
    position: absolute;
    width: 936px; height: 632px;
    transform: scale(0.8);
    transform-origin: 0 0;
    overflow: hidden;
    background: var(--white);
    font-family: "Lato", sans-serif;
    color: var(--white);
  }
  .postcard--front { left: 225.6px; top: 85.6px; }
  .postcard--back  { left: 225.6px; top: 638.4px; }
  .shapes { position: absolute; inset: 0; width: 936px; height: 632px; }
  .abs { position: absolute; margin: 0; }

  .brand {
    display: flex; align-items: center; gap: 8px;
    font-family: "Lato", sans-serif; font-weight: 700;
    font-size: 24px; line-height: 1; white-space: nowrap;
  }
  .brand__dot { width: 14px; height: 14px; border-radius: 50%; }
  .brand--light { color: var(--white); }
  .brand--light .brand__dot { background: var(--white); }
  .brand--dark { color: var(--pink); }
  .brand--dark .brand__dot { background: var(--blue); }

  .headline { left: 42px; top: 205px; font-family: "Roboto Condensed", sans-serif; font-weight: 700; text-transform: uppercase; line-height: 0.88; }
  .headline__kicker { display: block; font-size: 32px; margin-bottom: 10px; }
  .headline__main { display: block; font-size: 66px; line-height: 0.9; }
  .lead {
    left: 44px; top: 376px; width: 380px;
    padding-left: 12px; border-left: 3px solid var(--white);
    font-size: 17.5px; line-height: 1.27;
  }
  .perks { left: 46px; top: 476px; display: flex; gap: 56px; }
  .perk { display: flex; align-items: center; gap: 10px; font-size: 19px; line-height: 1.2; }
  .perk svg { width: 40px; height: 40px; }

  .contact { display: flex; flex-direction: column; }
  .contact__phone { display: flex; align-items: center; gap: 12px; font-size: 34px; line-height: 1; }
  .contact__phone svg { width: 46px; height: 46px; flex: none; }
  .contact__line { font-size: 19px; line-height: 1.27; padding-left: 58px; }
  .contact--front { left: 598px; top: 512px; }
  .contact--back { left: 44px; top: 510px; }
  .contact--back .contact__phone { font-size: 33px; }

  .services { left: 46px; top: 110px; width: 440px; }
  .service { margin-bottom: 18px; }
  .service h3 { margin: 0 0 6px; font-size: 15px; font-weight: 400; letter-spacing: 0.2px; }
  .service p {
    margin: 0; padding-left: 11px; border-left: 3px solid var(--white);
    font-size: 10.6px; line-height: 1.28;
  }
  .service--wide p { width: 440px; }

  .photo { position: absolute; }
</style>
</head>
<body>

<section class="postcard postcard--front" aria-label="Postcard front">
  <svg class="shapes" viewBox="0 0 936 632" aria-hidden="true">
    <polygon points="300,0 936,0 936,632 300,632" fill="#8d3f6e"/>
  </svg>
  <div class="photo" role="img" aria-label="Photo of a colourfully painted wheelie bin against a graffiti wall" style="left:330px;top:0;width:606px;height:632px;background:linear-gradient(135deg,#b9c3cf 0%,#e0468c 35%,#3aa06a 60%,#f08a3a 80%,#2c7a45 100%);"></div>
  <svg class="shapes" viewBox="0 0 936 632" aria-hidden="true">
    <polygon points="0,0 348,0 480,131 0,131" fill="var(--blue)"/>
    <rect x="298" y="70" width="52" height="5" fill="var(--pink)"/>
    <polygon points="868,0 936,0 936,128" fill="var(--ink)"/>
    <polygon points="0,131 480,131 510,175 0,175" fill="var(--band-grey)"/>
    <polygon points="0,553 382,553 368,598 0,598" fill="var(--band-grey)"/>
    <polygon points="0,565 530,565 525,632 0,632" fill="var(--blue)"/>
    <polygon points="0,175 395,175 513,353 395,553 0,553" fill="var(--pink)"/>
    <polygon points="445,195 460,195 513,353 495,353" fill="var(--white)" opacity="0.9"/>
    <polygon points="563,495 936,495 936,632 530,632" fill="var(--pink)"/>
  </svg>

  <div class="abs brand brand--light" style="left:84px;top:70px;"><span class="brand__dot"></span>Tello Haulage</div>

  <h1 class="abs headline">
    <span class="headline__kicker">Relax.</span>
    <span class="headline__main">We do the<br>dirty work</span>
  </h1>
  <p class="abs lead">Junk, clutter, debris, rubbish, trash, hogwash, garbage and scrap… whatever you're under, we're here to help clean it out.</p>
  <div class="abs perks">
    <div class="perk">
      <svg viewBox="0 0 40 40"><circle cx="20" cy="20" r="17" fill="none" stroke="#fff" stroke-width="2.5"/><path d="M11 20l7 7 15-17" fill="none" stroke="#fff" stroke-width="3" stroke-linecap="round" stroke-linejoin="round"/></svg>
      <span>Core<br>Services</span>
    </div>
    <div class="perk">
      <svg viewBox="0 0 40 40"><circle cx="20" cy="20" r="17" fill="none" stroke="#fff" stroke-width="2.5"/><path d="M11 20l7 7 15-17" fill="none" stroke="#fff" stroke-width="3" stroke-linecap="round" stroke-linejoin="round"/></svg>
      <span>Free<br>Estimate</span>
    </div>
  </div>

  <div class="abs contact contact--front">
    <div class="contact__phone">
      <svg viewBox="0 0 46 46"><circle cx="23" cy="23" r="23" fill="#fff"/><path d="M15 12c2-1 3 0 4 2l2 4c1 2 0 3-1 4l-1 1c1 3 4 6 7 7l1-1c1-1 2-2 4-1l4 2c2 1 3 2 2 4-1 3-4 4-7 3-7-2-13-8-15-15-1-3 0-6 0-10z" fill="var(--pink)"/></svg>
      <span>555-014-7328</span>
    </div>
    <span class="contact__line">info@tellohaulage.example</span>
    <span class="contact__line">www.tellohaulage.example</span>
  </div>
</section>

<section class="postcard postcard--back" aria-label="Postcard back">
  <div class="photo" role="img" aria-label="Photo of stacked wooden pallets and corrugated metal sheets" style="left:0;top:0;width:380px;height:100px;background:linear-gradient(90deg,#b7bcc2 0%,#7a5a3e 45%,#4a3322 100%);"></div>
  <svg class="shapes" viewBox="0 0 936 632" aria-hidden="true">
    <polygon points="316,0 463,0 406,135" fill="var(--ink)"/>
    <polygon points="0,95 350,95 406,135 440,60 513,355 398,495 0,495" fill="var(--blue)"/>
    <polygon points="0,95 350,95 406,135 0,135" fill="var(--blue-deep)" opacity="0.35"/>
    <polygon points="0,495 398,495 453,632 0,632" fill="var(--pink)"/>
    <polygon points="405,495 418,495 460,600 452,610" fill="var(--white)" opacity="0.85"/>
    <rect x="805" y="42" width="88" height="100" fill="var(--stamp)"/>
    <g stroke="var(--rule)" stroke-width="1.2">
      <line x1="576" y1="223" x2="890" y2="223"/>
      <line x1="576" y1="317" x2="890" y2="317"/>
      <line x1="576" y1="410" x2="890" y2="410"/>
      <line x1="576" y1="502" x2="890" y2="502"/>
    </g>
  </svg>

  <div class="abs brand brand--dark" style="left:508px;top:74px;"><span class="brand__dot"></span>Tello Haulage</div>

  <div class="abs services">
    <div class="service">
      <h3>RESIDENTIAL</h3>
      <p>From getting your garage back to good and sloughing out storage<br>units to attacking the attic, we are here to help you reclaim that<br>sweet square footage.</p>
    </div>
    <div class="service">
      <h3>COMMERCIAL</h3>
      <p>Outfitting your retail space or overhauling the office?<br>Let's get to work.<br>We've got you covered for those large scale clean ups and hauls.</p>
    </div>
    <div class="service">
      <h3>OUTSIDE</h3>
      <p>Time to get rid of<br>that old hot tub, rotting shed or a playset the kids have outgrown?<br>Nix the hassle and let us do the heavy lifting.</p>
    </div>
    <div class="service service--wide">
      <h3>CURBSIDE</h3>
      <p>Do you have a oversized item or pile on your curb your trash truck wouldn't pickup?<br>We don't scare easy and are here to help with those bulky items.</p>
    </div>
    <div class="service">
      <h3>OTHER</h3>
      <p>Need help with some other projects that may not fit in the scope of our<br>primary services?<br>Take a look at what else we can offer!</p>
    </div>
  </div>

  <div class="abs contact contact--back">
    <div class="contact__phone">
      <svg viewBox="0 0 46 46"><circle cx="23" cy="23" r="23" fill="#fff"/><path d="M15 12c2-1 3 0 4 2l2 4c1 2 0 3-1 4l-1 1c1 3 4 6 7 7l1-1c1-1 2-2 4-1l4 2c2 1 3 2 2 4-1 3-4 4-7 3-7-2-13-8-15-15-1-3 0-6 0-10z" fill="var(--pink)"/></svg>
      <span>555-014-7328</span>
    </div>
    <span class="contact__line">info@tellohaulage.example</span>
    <span class="contact__line">www.tellohaulage.example</span>
  </div>
</section>

</body>
</html>
```